Beauty Therapy Web Design

I need a web page design for a small beauty therapy clinic, the owner is currently the only beauty therapist working there.
We require the following pages:
Home
About
Treatments
Nails
Courses
Contact
I will attach the clinics business card, treatment menu and signage so that you get a feeling for the branding colours etc.
This is the first website for the beauty therapist, she would like to attract new clients and also tourists that come in on the cruise ships. The thing that sets her apart from other clinics is that she welcomes texting for appointments.
I have selected refundable because I have never done this before so I don't know what to expect, I have the full intention of going through with it as long as I get a good design.
Feel free to ask for further information
Reason: Project extended as I am away for work and am unable to meet with the owner.
Target Market(s)
Females 18 to 50
Industry/Entity Type
Business
Look and feel
Each slider illustrates characteristics of the customer's brand and the style your logo design should communicate.

```html
<!DOCTYPE html>
<html lang="en">
<head>
<meta charset="utf-8">
<title>Lumina Beauty Therapy</title>
<link href="https://fonts.googleapis.com/css2?family=Cinzel:wght@400&family=Ubuntu:wght@300;400;500&display=swap" rel="stylesheet">
<style>
:root{
  --purple:#7d68b4;
  --purple-dark:#5f4c99;
  --purple-light:#9a88cc;
  --bg-top:#8a76c0;
  --bg-bottom:#7a66b2;
  --ink:#333;
  --muted:#555;
  --red:#b3262e;
  --white:#fff;
  --panel:#f7f6f9;
}
*{margin:0;padding:0;box-sizing:border-box}
html,body{width:766px;height:1200px;overflow:hidden}
body{position:relative;background:linear-gradient(180deg,var(--bg-top),var(--bg-bottom));font-family:"Ubuntu",sans-serif;color:var(--ink)}
.abs{position:absolute}
.header-card{left:28px;top:24px;width:710px;height:120px;background:var(--white);border-radius:10px 10px 0 0}
.brand-name{left:52px;top:42px;font-family:"Cinzel",serif;color:var(--purple);font-size:30px;line-height:1}
.brand-sub{left:52px;top:88px;font-family:"Cinzel",serif;color:var(--purple);font-size:17px;letter-spacing:.5px;line-height:1}
.phone-icon{left:566px;top:46px;width:23px;height:23px;border-radius:4px;background:var(--purple-dark)}
.phone-number{left:596px;top:47px;font-size:16px;color:var(--purple-dark);line-height:1.3}
.search{left:565px;top:86px;width:129px;height:28px;background:linear-gradient(#fff,#eceaf0);border-radius:3px 0 0 3px}
.search span{position:absolute;left:32px;top:9px;font-size:8px;color:#777}
.search svg{position:absolute;left:8px;top:5px}
.search-go{left:694px;top:86px;width:31px;height:28px;background:var(--purple);color:#fff;font-size:9px;font-weight:500;text-align:center;line-height:28px;border-radius:0 3px 3px 0}
.nav{left:28px;top:134px;width:710px;height:32px;background:linear-gradient(#9784c9,#7763b0);border-radius:0 0 10px 10px;display:flex}
.nav a{position:absolute;top:0;height:32px;line-height:32px;color:#fff;font-size:8.6px;text-decoration:none}
.nav .active{background:var(--purple-light);top:-6px;height:38px;line-height:44px;padding:0 9px}
.main-card{left:28px;top:173px;width:706px;height:903px;background:var(--white);border-radius:0 0 10px 10px}
.hero{left:28px;top:173px;width:706px;height:320px;background:linear-gradient(100deg,#d9b39d 0%,#efe2da 35%,#f6f4f3 60%,#e4c8b3 100%)}
.hero-text{left:438px;top:262px;width:200px;font-size:8.8px;line-height:22px;color:#222}
.hero-btn{left:443px;top:338px;width:115px;height:35px;background:linear-gradient(#8d79c3,#6a57a7);color:#fff;font-size:9px;font-weight:500;text-align:center;line-height:35px;border-radius:3px}
.arrow{width:22px;height:22px;border-radius:50%;background:#fff;border:2px solid #222}
.welcome{left:398px;top:460px;font-size:15px;color:var(--purple-dark)}
.dots{left:400px;top:486px;width:230px;border-top:1px dotted #777}
.shop-photo{left:45px;top:507px;width:245px;height:141px;background:linear-gradient(#3b2f6e 0%,#5a4a93 25%,#8d8a84 45%,#4b4a47 100%);border:1px solid var(--purple)}
.intro{left:300px;top:505px;width:430px;font-size:8px;line-height:17.6px;color:#444}
.intro p+p{margin-top:17.6px}
.more-red{left:664px;top:643px;font-size:8px;color:var(--red)}
.sidebar{left:47px;top:693px;width:181px;height:234px;border:1px solid var(--purple);background:#fff}
.sidebar h3{height:35px;background:var(--purple);color:#fff;font-weight:400;font-size:9.5px;line-height:35px;padding-left:24px}
.sidebar li{list-style:none;height:30.6px;line-height:30px;font-size:9px;color:#555;padding-left:24px;border-bottom:1px solid #e3e3e3;position:relative}
.sidebar li:last-child{border:0}
.sidebar li::before{content:"";position:absolute;left:14px;top:12px;border-left:4px solid #444;border-top:3px solid transparent;border-bottom:3px solid transparent}
.appointment{left:45px;top:942px;width:185px;height:68px;background:linear-gradient(#fff,#f1f0f4);border-radius:4px;box-shadow:0 1px 3px rgba(0,0,0,.15)}
.appointment h4{position:absolute;left:54px;top:20px;font-weight:400;font-size:12.5px;color:var(--purple-dark)}
.appointment span{position:absolute;left:55px;top:43px;font-size:8.2px;color:#222}
.appointment svg{position:absolute;left:10px;top:22px}
.gallery-title{left:260px;top:690px;font-size:12.5px;color:#444}
.g-head{font-size:11px;color:var(--purple)}
.g-img{width:181px;height:112px;border:3px solid #fff;box-shadow:0 0 2px rgba(0,0,0,.35)}
.g-more{font-size:7.5px;color:var(--purple)}
.footer-title{font-size:10.5px;color:#fff}
.mail-input{left:34px;top:1121px;width:155px;height:18px;background:#fff;border:1px solid #ccc;font-size:7.5px;font-style:italic;color:#999;padding:4px 0 0 10px}
.submit{left:34px;top:1154px;width:47px;height:16px;background:#1c1c1c;color:#fff;font-size:8px;text-align:center;line-height:16px;border-radius:3px}
.links{font-size:7.8px;color:#efeaf8;line-height:14.8px}
.social{top:1099px;width:20px;height:20px;border-radius:50%;background:#fff}
.connect{left:556px;top:1104px;font-size:7.8px;color:#fff}
.copyright{left:560px;top:1140px;font-size:7.8px;color:#fff}
</style>
</head>
<body>
<div class="abs header-card"></div>
<div class="abs brand-name">Lumina</div>
<div class="abs brand-sub">BEAUTY THERAPY</div>
<div class="abs phone-icon">
  <svg width="23" height="23" viewBox="0 0 23 23"><path d="M9 6c-1 0-2 1-2 2 0 4 3 8 7 9 1 0 2-1 2-2l-2-1-1 1c-2-1-3-2-4-4l1-1z" fill="none" stroke="#fff" stroke-width="1.2"/></svg>
</div>
<div class="abs phone-number">555 014 2290</div>
<div class="abs search">
  <svg width="18" height="18" viewBox="0 0 18 18"><circle cx="7" cy="7" r="5" fill="none" stroke="#7a8ab0" stroke-width="2"/><line x1="11" y1="11" x2="16" y2="16" stroke="#7a8ab0" stroke-width="2.5"/></svg>
  <span>Search</span>
</div>
<div class="abs search-go">GO</div>

<nav class="abs nav">
  <a style="left:24px">HOME</a>
  <a class="active" style="left:69px">ABOUT US</a>
  <a style="left:148px">BLOG</a>
  <a style="left:198px">PRODUCTS</a>
  <a style="left:269px">GALLERY</a>
  <a style="left:334px">PACKAGES &amp; SERVICES</a>
  <a style="left:454px">TESTIMONIALS</a>
  <a style="left:539px">CONTACT US</a>
</nav>

<div class="abs main-card"></div>
<div class="abs hero" role="img" aria-label="Close-up of make-up being applied with an applicator brush"></div>
<svg class="abs" style="left:28px;top:390px" width="706" height="120" viewBox="0 0 706 120">
  <path d="M0,50 C150,120 300,110 430,55 C540,10 640,15 706,48 L706,120 L0,120Z" fill="#fff"/>
  <path d="M0,50 C150,120 300,110 430,55 C540,10 640,15 706,48 L706,55 C640,28 540,25 440,62 C310,112 150,120 0,60Z" fill="#8a76c0"/>
</svg>
<div class="abs hero-text">Lorem ipsum dolor sit amet,consectetuer adipiscing elit. Lorem ipsum dolor sit amet,consectetuer adipiscing elit.</div>
<div class="abs hero-btn">FIND OUT MORE</div>
<div class="abs arrow" style="left:27px;top:288px"><svg width="18" height="18"><path d="M7 6l3 3-3 3" fill="none" stroke="#222" stroke-width="1.3"/></svg></div>
<div class="abs arrow" style="left:714px;top:288px"><svg width="18" height="18"><path d="M11 6l-3 3 3 3" fill="none" stroke="#222" stroke-width="1.3"/></svg></div>

<h1 class="abs welcome" style="font-weight:400">Welcome to Lumina Beauty Therapy</h1>
<div class="abs dots"></div>
<div class="abs shop-photo" role="img" aria-label="Shop front of the clinic with its purple sign"></div>
<div class="abs intro">
  <p>Nunc varius facilisis eros. Sed erat. In in velit quis arcu ornare laoreet. Nunc varius facilisis eros. Sed erat. In in velit quis arcu ornare laoreet. Nunc varius facilisis eros. Sed erat. In in velit quis arcu ornare laoreet. Nunc varius facilisis eros. Sed erat. In in velit quis arcu ornare laoreet. Nunc varius facilisis eros. Sed erat. In in velit quis arcu ornare laoreet. Nunc varius facilisis eros. Sed erat. In in velit quis arcu ornare laoreet. Nunc varius facilisis eros. Sed erat.</p>
  <p>In in velit quis arcu ornare laoreet. Nunc varius facilisis eros. Sed erat. In in velit quis arcu ornare laoreet. Nunc varius facilisis eros. Sed erat. In in velit quis arcu ornare laoreet. Nunc varius facilisis eros. Sed erat. In in velit quis arcu ornare laoreet. Nunc varius facilisis eros. Sed erat. In in velit quis arcu ornare laoreet.</p>
</div>
<div class="abs more-red">View More &gt;&gt;</div>

<aside class="abs sidebar">
  <h3>Beauty Therapy</h3>
  <ul>
    <li>Facials</li><li>Waxing</li><li>Acrylic &amp; Gel Nails</li><li>Eye lash ? Brow tints</li><li>Manicures ? Pedicures</li><li>Spray tans</li>
  </ul>
</aside>
<div class="abs appointment">
  <svg width="42" height="30" viewBox="0 0 42 30"><path d="M4 6 L36 2 L40 26 L8 29Z" fill="#fff" stroke="#4a6aa8" stroke-width="1.3"/><path d="M4 6 L36 2 L37 9 L5 12Z" fill="#4a6aa8"/></svg>
  <h4>Quick Appointment</h4>
  <span>YOUR APPOINTMENT &gt;&gt;</span>
</div>

<h2 class="abs gallery-title" style="font-weight:400">Gallery</h2>
<div class="abs g-head" style="left:262px;top:716px">Mens Waxing</div>
<div class="abs g-img" role="img" aria-label="Wax being applied to a man's back" style="left:262px;top:741px;background:linear-gradient(135deg,#3a3634,#b08f78 50%,#d9b59c)"></div>
<div class="abs g-more" style="left:266px;top:865px">View More &gt;&gt;</div>
<div class="abs g-head" style="left:484px;top:716px">Massage</div>
<div class="abs g-img" role="img" aria-label="Relaxing back massage with rose petals" style="left:484px;top:741px;background:linear-gradient(180deg,#8fb4dc,#d6c2b3 55%,#9b3030)"></div>
<div class="abs g-more" style="left:488px;top:865px">View More &gt;&gt;</div>
<div class="abs g-head" style="left:266px;top:897px">Facials</div>
<div class="abs g-img" role="img" aria-label="Facial mask treatment" style="left:265px;top:922px;background:linear-gradient(135deg,#3a2a20,#a0705a 45%,#e2ddd8 60%,#6a4a3a)"></div>
<div class="abs g-more" style="left:270px;top:1045px">View More &gt;&gt;</div>
<div class="abs g-head" style="left:488px;top:897px">Gel Toe Nails</div>
<div class="abs g-img" role="img" aria-label="Decorated gel toe nails with a pink rose" style="left:487px;top:922px;background:linear-gradient(135deg,#b7a7d8,#e6b7a6 50%,#c83a6a)"></div>
<div class="abs g-more" style="left:492px;top:1045px">View More &gt;&gt;</div>

<svg class="abs" style="left:38px;top:1092px" width="18" height="13"><rect x="0.5" y="0.5" width="17" height="12" fill="#dcd6ee" stroke="#fff"/><path d="M1 1l8 6 8-6" fill="none" stroke="#fff"/></svg>
<div class="abs footer-title" style="left:63px;top:1091px">Mailing List</div>
<div class="abs mail-input">Enter your mail ID</div>
<div class="abs submit">SUBMIT</div>

<div class="abs footer-title" style="left:260px;top:1090px">Important Links</div>
<div class="abs links" style="left:259px;top:1114px">Waxing<br>Mens Waxing<br>Beautiful Eyes<br>Facials<br>Spray on Tan</div>
<div class="abs links" style="left:363px;top:1114px">Manicure<br>Pedicure<br>Massage<br>Nail<br>Enhancement</div>
<div class="abs links" style="left:453px;top:1114px">Privacy<br>Terms<br>Contact</div>

<div class="abs connect">Connect with us :</div>
<div class="abs social" style="left:630px"></div>
<div class="abs social" style="left:655px"></div>
<div class="abs social" style="left:680px"></div>
<div class="abs social" style="left:706px"></div>
<div class="abs copyright">Copyright © 2012 Lumina,All rights reserved</div>
</body>
</html>
```